A5 brochure for a double glazed window company - design only

We have an a4 brochure currently and would like to go to an A5 and revamp it. We are a business in Canberra, Australia and it is handed out to the public. It will be 3 A5 sheets back to back to make a 6 page booklet with front and back covers. There will be photos and graphics.

We love our current brochure and can provide it for inspiration - we always get great feedback on the brochure. Happy to have some improvements to take it to the next level.

Documents will be provided once successful with the tender.

Our website is www.brindlepane.com.au
facebook social: @brindlepane

Target Market(s)

People wanting to have a more energy efficient home through double glazing

Industry/Entity Type

Construction

Font styles to use
Sans Serif

Colors
33a6d7
3377b5
0355a3
85cae6
cee9f5
cedeed
eaf1f7
0292cd

Requirements
Must have
• A perception of confidence and pull the reader to book an appointment with us. Authorities on double glazing
Nice to have
• lots of soothing blues
Should not have
• tones outside of blues, greys, black
• The brochure I have attached is merely for looks and the front and back pages - content is changing.

```html
<!DOCTYPE html>
<html lang="en">
<head>
<meta charset="utf-8">
<title>Brindle Pane – A5 Brochure</title>
<link href="https://fonts.googleapis.com/css2?family=Open+Sans:wght@400;600;700&display=swap" rel="stylesheet">
<style>
:root{
  --sky:#33a6d7;
  --mid:#3377b5;
  --navy:#0355a3;
  --pale:#85cae6;
  --mist:#cee9f5;
  --frost:#cedeed;
  --ice:#eaf1f7;
  --bright:#0292cd;
  --ink:#2c3e50;
  --stage:#2e3033;
}
*{box-sizing:border-box;margin:0;padding:0}
html,body{width:900px;height:1200px;overflow:hidden}
body{background:var(--stage);font-family:'Open Sans',Arial,sans-serif;color:var(--ink);position:relative}
.spread{position:absolute;left:15px;width:870px;display:flex;box-shadow:0 6px 18px rgba(0,0,0,.45)}
.spread--outer{top:110px;height:660px}
.spread--inner{top:790px;height:400px}
.panel{position:relative;width:290px;height:100%;overflow:hidden}
p{font-size:10.4px;line-height:1.5;margin-bottom:9px}

/* outer left */
.panel--why{background:#fff;padding:62px 20px 20px}
.why-band{position:absolute;top:14px;left:0;width:100%;height:34px}
.why-title{position:absolute;top:22px;left:22px;color:#fff;font-weight:700;font-size:14px}

/* outer middle */
.panel--contact{background:var(--navy)}
.contact-photo{position:absolute;top:0;left:0;width:100%;height:250px;background:linear-gradient(160deg,var(--frost),var(--pale) 45%,var(--mid))}
.contact-wedge{position:absolute;top:215px;left:0;width:100%;height:80px}
.contact-title{position:absolute;top:275px;left:120px;background:var(--sky);color:#fff;font-weight:700;font-size:14px;padding:5px 14px}
.contact-list{position:absolute;top:325px;left:22px;right:16px;list-style:none}
.contact-list li{display:flex;align-items:center;gap:10px;color:#fff;font-size:10.5px;margin-bottom:16px}
.contact-list svg{flex:none}
.contact-lower{position:absolute;bottom:0;left:0;width:100%;height:220px;background:linear-gradient(180deg,rgba(3,85,163,0),rgba(51,119,181,.55))}

/* cover */
.panel--cover{background:#fff}
.brand{position:absolute;top:26px;left:36px;display:flex;align-items:center;gap:12px}
.brand-mark{width:30px;height:30px;border-radius:50%;background:var(--bright)}
.brand-name{font-size:26px;font-weight:600;color:var(--mid)}
.tagline{position:absolute;top:70px;left:78px;font-size:12px;color:var(--navy);line-height:1.3}
.cover-photo{position:absolute;background:linear-gradient(150deg,var(--ice),var(--pale) 55%,var(--mid))}
.cover-photo--a{top:120px;left:22px;width:120px;height:200px}
.cover-photo--b{top:120px;left:150px;width:120px;height:200px;background:linear-gradient(200deg,var(--frost),var(--sky) 60%,var(--navy))}
.cover-photo--c{top:330px;left:22px;width:248px;height:180px;background:linear-gradient(170deg,var(--mist),var(--pale) 40%,var(--mid))}
.cover-band{position:absolute;bottom:0;left:0;width:100%;height:150px}
.cover-cta{position:absolute;bottom:40px;left:30px;color:#fff;font-size:10px;font-weight:600}

/* inner */
.panel--about{background:#fff;padding:14px 16px}
.head-bar{display:inline-block;background:var(--sky);color:#fff;font-weight:700;font-size:11px;padding:4px 10px;margin-bottom:7px}
.panel--about p,.panel--criteria p,.panel--ceo p{font-size:9.6px;line-height:1.45;margin-bottom:7px}
.frames{list-style:none}
.frames li{font-size:9.6px;line-height:1.45;margin-bottom:3px;padding-left:10px;position:relative}
.frames li::before{content:"";position:absolute;left:0;top:6px;width:4px;height:4px;background:var(--sky)}
.panel--criteria{background:linear-gradient(180deg,var(--bright),var(--mid));padding:14px 16px;color:#fff}
.criteria-title{background:var(--navy);font-weight:700;font-size:11px;line-height:1.35;padding:6px 10px;margin-bottom:10px}
.panel--ceo{background:var(--ice);padding:14px 16px}
.ceo-title{display:inline-block;background:var(--navy);color:#fff;font-weight:700;font-size:11px;padding:4px 10px;margin-bottom:8px}
.ceo-corner{position:absolute;bottom:0;right:0}
</style>
</head>
<body>

<section class="spread spread--outer">
  <article class="panel panel--why">
    <svg class="why-band" viewBox="0 0 290 34" preserveAspectRatio="none"><path d="M0 0H250Q290 17 250 34H0Z" fill="var(--sky)"/></svg>
    <h2 class="why-title">Why Brindle Pane?</h2>
    <p>Brindle Pane has been helping Canberra homes stay warm in winter and cool in summer for many years. Our local team handles every step, from the first measure to the final clean up.</p>
    <p>Every window we install is built to suit the home, the climate and the way you live. We use quality glass, strong frames and careful fitting so the result lasts for decades.</p>
    <p>Double glazing cuts heat loss, blocks street noise and reduces condensation on cold mornings, so your rooms feel calmer and more comfortable all year round.</p>
    <p>We explain the options clearly and give honest advice, with no pressure and no hidden costs in the quote.</p>
    <p>Our windows are made to Australian standards and backed by a full warranty, so you can buy with confidence and enjoy the benefits for years to come.</p>
    <p>We can also upgrade your existing frames with new glass, a simple option that keeps the look of your home while lifting its comfort.</p>
    <p>Book a free visit and see how much you could save on energy bills.</p>
  </article>

  <article class="panel panel--contact">
    <div class="contact-photo" role="img" aria-label="Photo of a modern home with large double glazed windows"></div>
    <svg class="contact-wedge" viewBox="0 0 290 80" preserveAspectRatio="none"><path d="M0 40L290 0V80H0Z" fill="var(--navy)"/><path d="M0 40L290 0V8L0 48Z" fill="var(--sky)"/></svg>
    <div class="contact-lower"></div>
    <h2 class="contact-title">Contact details</h2>
    <ul class="contact-list">
      <li><svg width="22" height="22" viewBox="0 0 22 22"><circle cx="11" cy="11" r="11" fill="var(--sky)"/><path d="M7 6l2.5-.5 1.2 3-1.5 1a7 7 0 003.3 3.3l1-1.5 3 1.2L16 15c-5 0-9-4-9-9z" fill="#fff"/></svg>(02) 6100 4820</li>
      <li><svg width="22" height="22" viewBox="0 0 22 22"><circle cx="11" cy="11" r="11" fill="var(--sky)"/><circle cx="11" cy="11" r="6" fill="none" stroke="#fff" stroke-width="1.3"/><path d="M5 11h12M11 5c-3 3-3 9 0 12M11 5c3 3 3 9 0 12" fill="none" stroke="#fff" stroke-width="1.1"/></svg>www.brindlepane.com.au</li>
      <li><svg width="22" height="22" viewBox="0 0 22 22"><rect width="22" height="22" fill="var(--sky)"/></svg>social: @brindlepane</li>
    </ul>
  </article>

  <article class="panel panel--cover">
    <div class="brand"><span class="brand-mark"></span><span class="brand-name">Brindle Pane</span></div>
    <div class="tagline">Save money<br>Save energy</div>
    <div class="cover-photo cover-photo--a" role="img" aria-label="Photo of a tall double glazed window"></div>
    <div class="cover-photo cover-photo--b" role="img" aria-label="Photo of window glass reflecting sky"></div>
    <div class="cover-photo cover-photo--c" role="img" aria-label="Photo of a bright living room with large windows"></div>
    <svg class="cover-band" viewBox="0 0 290 150" preserveAspectRatio="none"><path d="M0 40L290 0V150H0Z" fill="var(--sky)"/><path d="M0 70L290 30V150H0Z" fill="var(--mid)"/></svg>
    <div class="cover-cta">Call us now to get a free quote!</div>
  </article>
</section>

<section class="spread spread--inner">
  <article class="panel panel--about">
    <h2 class="head-bar">About double glazing</h2>
    <p>One of the best things you can do for your home is to add double glazing. Two panes of glass with a sealed gap between them trap heat inside during winter and keep it out in summer. It also lowers noise, reduces condensation and protects floors from fading. It is a smart long term investment that adds value and comfort.</p>
    <h2 class="head-bar">Frames we offer</h2>
    <ul class="frames">
      <li>Standard Aluminium – a slim, strong frame with a clean modern look.</li>
      <li>Thermally Broken Aluminium – an insulated core that stops heat moving through the frame.</li>
      <li>uPVC – excellent insulation with very low upkeep.</li>
      <li>Timber – natural warmth and classic style.</li>
    </ul>
  </article>

  <article class="panel panel--criteria">
    <h2 class="criteria-title">What are the key performance criteria to consider with double glazing?</h2>
    <p>The most important figure is the U-value, which measures how much heat moves through the whole window. The lower the number, the better the window keeps your home warm.</p>
    <p>Next is the Solar Heat Gain Coefficient, which shows how much of the sun's heat passes through the glass. A low figure suits west facing rooms, while a higher figure helps in winter.</p>
    <p>Finally, look at air leakage and the quality of the seals, because even the best glass cannot perform in a draughty frame. Ask us to explain the ratings for each window we quote.</p>
  </article>

  <article class="panel panel--ceo">
    <h2 class="ceo-title">Message from the CEO</h2>
    <p>We started this business because we wanted Canberra families to enjoy homes that are comfortable in every season. Our team takes pride in careful work and clear advice.</p>
    <p>We measure, build and fit every window ourselves, so we can stand behind the result. Thank you for considering us, and we look forward to helping you create a warmer, quieter and more efficient home.</p>
    <ul class="frames"><li>Enjoy a more comfortable home all year round</li></ul>
    <svg class="ceo-corner" width="120" height="60" viewBox="0 0 120 60"><path d="M120 0V60H0Z" fill="var(--pale)"/><path d="M120 20V60H40Z" fill="var(--sky)"/></svg>
  </article>
</section>

</body>
</html>
```